Vanta-Ride Transit private ambulance flyer/broshure

I need a Tri-fold brochure for our BLS non-emergency private ambulance company. We transport patients to doctors appointments, hyperbarics, dialysis, out of town doctors appointment and scheduled medical procedures etc.

```html
<!DOCTYPE html>
<html lang="en">
<head>
<meta charset="utf-8">
<title>Vanta-Ride Transit Tri-fold Brochure</title>
<link href="https://fonts.googleapis.com/css2?family=Oswald:wght@600;700&family=Arimo:wght@400;700&display=swap" rel="stylesheet">
<style>
  :root {
    --page-bg: #f2f2f2;
    --sky-blue: #9ccfe9;
    --sky-blue-deep: #86bddc;
    --white: #ffffff;
    --soft-white: rgba(255,255,255,0.82);
    --brand-navy: #2d3a8c;
    --alert-red: #b8302d;
    --steel-blue: #5c8fb8;
    --cover-frame: #6f9fbf;
  }
  * { box-sizing: border-box; margin: 0; padding: 0; }
  html, body { width: 1200px; height: 1200px; overflow: hidden; background: var(--page-bg); }
  .brochure {
    position: absolute; left: 30px; top: 195px;
    width: 1140px; height: 810px;
    display: flex;
    box-shadow: 0 6px 24px rgba(0,0,0,0.18);
  }
  .panel { position: relative; width: 380px; height: 810px; overflow: hidden; }

  /* Left panel */
  .panel-inside { background: #6d7a8a; }
  .panel-inside .photo {
    position: absolute; inset: 0;
    background: linear-gradient(160deg, #56687a 0%, #8fb7c9 28%, #d98a94 55%, #e2646f 72%, #c94d5a 100%);
  }
  .panel-inside .copy {
    position: absolute; left: 58px; width: 285px;
    font-family: "Arimo", sans-serif; color: var(--white);
    font-size: 15px; line-height: 20px;
  }
  .panel-inside .copy-top { top: 50px; font-weight: 700; }
  .panel-inside .copy-bottom { top: 535px; }

  /* Middle panel */
  .panel-contact { background: linear-gradient(180deg, var(--sky-blue) 0%, var(--sky-blue-deep) 100%); padding: 0 38px; }
  .contact-head { display: flex; align-items: flex-start; margin-top: 48px; height: 90px; }
  .brand-mark { display: flex; align-items: center; gap: 8px; width: 175px; margin-top: 14px; }
  .brand-mark .dot { width: 22px; height: 22px; border-radius: 50%; background: var(--brand-navy); flex: none; }
  .brand-name {
    font-family: "Oswald", sans-serif; font-weight: 700; color: var(--brand-navy);
    font-size: 20px; line-height: 22px; letter-spacing: 0.3px;
  }
  .service-tags {
    font-family: "Oswald", sans-serif; font-weight: 700; color: var(--white);
    font-size: 38px; line-height: 40px; margin-left: 20px;
  }
  .contact-tagline {
    font-family: "Oswald", sans-serif; font-weight: 700; color: var(--white);
    font-size: 25px; letter-spacing: 0.5px; margin-top: 18px;
  }
  .rule { height: 16px; background: #e9edf0; margin-top: 24px; }
  .contact-list { font-family: "Arimo", sans-serif; color: var(--soft-white); margin: 26px 0 34px; }
  .contact-list dt { font-size: 22px; line-height: 28px; }
  .contact-list dd { font-size: 24px; line-height: 34px; font-weight: 700; margin-bottom: 0; }
  .contact-body {
    font-family: "Arimo", sans-serif; color: var(--soft-white);
    font-size: 15px; line-height: 20px; margin-top: 44px;
  }

  /* Right panel (cover) */
  .panel-cover { background: var(--cover-frame); padding: 14px; }
  .cover-inner { position: relative; width: 100%; height: 100%; overflow: hidden; }
  .cover-inner .photo {
    position: absolute; inset: 0;
    background: linear-gradient(180deg, #2b3e44 0%, #51656b 25%, #c9a9a6 42%, #9aa7a8 55%, #4f6b4a 72%, #2f4236 88%, #1f2b2c 100%);
  }
  .cover-brand { position: absolute; left: 40px; top: 60px; display: flex; align-items: center; gap: 12px; }
  .cover-brand .dot { width: 40px; height: 40px; border-radius: 50%; background: var(--brand-navy); }
  .cover-brand .brand-name { font-size: 38px; line-height: 42px; color: var(--brand-navy); }
  .cover-services {
    position: absolute; left: 0; right: 0; top: 270px;
    font-family: "Oswald", sans-serif; font-weight: 700; color: var(--alert-red);
    font-size: 64px; line-height: 78px;
  }
  .cover-services span { display: block; }
  .cover-services .bls { margin-left: 88px; }
  .cover-services .acls { margin-left: 118px; }
  .cover-tagline {
    position: absolute; left: 0; right: 0; top: 640px;
    font-family: "Oswald", sans-serif; font-weight: 700; color: var(--steel-blue);
    font-size: 42px; line-height: 56px;
  }
  .cover-tagline span { display: block; }
  .cover-tagline .first { margin-left: 62px; }
  .cover-tagline .second { margin-left: 120px; }
</style>
</head>
<body>
  <main class="brochure">
    <section class="panel panel-inside">
      <div class="photo" role="img" aria-label="Photo of an ambulance with lights on inside a bright hospital corridor"></div>
      <p class="copy copy-top">Doluptam verovid moluptas sandam aut quatias volore se pro occabor sunt aut quam ipiendit is diam fugias et quodit volore earitae perspernam quas erio. Atem reic te issequiditem inti utem quam reribustrum voles-</p>
      <p class="copy copy-bottom">Doluptam verovid moluptas sandam aut quatias volore se pro occabor sunt aut quam ipiendit is diam fugias et quodit volore earitae perspernam quas erio. Atem reic te issequiditem inti utem quam reribustrum volessequi sumquas ex estibeat fugit quat faciaer ovitati rero ipsandis eos exerum qui inus ex erepudi aut alit officabor aut utem dolupta venihil mo et</p>
    </section>

    <section class="panel panel-contact">
      <div class="contact-head">
        <div class="brand-mark">
          <span class="dot"></span>
          <span class="brand-name">Vanta-Ride Transit</span>
        </div>
        <div class="service-tags">BLS<br>ACLS</div>
      </div>
      <h2 class="contact-tagline">TRANSFERS-DISCHARGES</h2>
      <div class="rule"></div>
      <dl class="contact-list">
        <dt>Office:</dt><dd>555-201-3370</dd>
        <dt>Fax:</dt><dd>555-201-3371</dd>
        <dt>After Hours:</dt><dd>555-201-3372</dd>
      </dl>
      <div class="rule"></div>
      <p class="contact-body">Doluptam verovid moluptas sandam aut quatias volore se pro occabor sunt aut quam ipiendit is diam fugias et quodit volore earitae perspernam quas erio. Atem reic te issequiditem inti utem quam reribustrum volessequi sumquas ex estibeat fugit quat faciaer ovitati rero ipsandis eos exerum qui inus ex erepudi aut alit officabor aut utem dolupta venihil mo et</p>
    </section>

    <section class="panel panel-cover">
      <div class="cover-inner">
        <div class="photo" role="img" aria-label="Photo of an ambulance driving on a mountain road under a cloudy sky"></div>
        <div class="cover-brand">
          <span class="dot"></span>
          <span class="brand-name">Vanta-Ride Transit</span>
        </div>
        <h1 class="cover-services"><span class="bls">BLS</span><span class="acls">ACLS</span></h1>
        <h2 class="cover-tagline"><span class="first">TRANSFERS</span><span class="second">DISCHARGES</span></h2>
      </div>
    </section>
  </main>
</body>
</html>
```